HVAC Company Business Card design with attached logo

Looking for an easily readable and attractive business card design that includes my attached company logo. I selected one sided card because it's more traditional, but I'm open to a 2-sided design. All of the details should be included in the design. Looking to create a professional, upscale image.

Target Market(s)

Commercial and residential consumers

Industry/Entity Type

Hvac

Contact Information for Business Card

Company phone number is 516.738.2945
Company email dennis@pinefieldhvac.example
Company name is Willow Creek Air Conditioning, Refrigeration, and Heating
Dennis Hartwell
Owner Operator
Company Address is
PO Box 782,
527 Tamsworth Rd,
Fernbrook, NY 11802
Business License H8179524000
Insured

Font styles to use
Serif
Sans Serif

Colors

Designer to choose colors to be used in the design.

Requirements
Must have
• Must include the logo.
Nice to have
• It seems like it should be a one sided card, but I'm open to a 2 sided one.

```html
<!DOCTYPE html>
<html lang="en">
<head>
<meta charset="utf-8">
<title>Willow Creek Air Conditioning, Refrigeration, and Heating – Business Card</title>
<link rel="stylesheet" href="https://fonts.googleapis.com/css2?family=Catamaran:wght@300;400;700;800&family=Questrial&display=swap">
<style>
  :root {
    --brand-blue: #2b50a3;
    --brand-orange: #f26a22;
    --orange-fold: #d9541a;
    --paper: #ffffff;
  }
  * { box-sizing: border-box; margin: 0; padding: 0; }
  html, body { width: 1200px; height: 686px; overflow: hidden; background: var(--paper); }
  .card {
    position: relative;
    width: 1200px;
    height: 686px;
    background: var(--paper);
    overflow: hidden;
    font-family: "Catamaran", sans-serif;
  }
  .card-shapes { position: absolute; inset: 0; }

  .brand {
    position: absolute;
    left: 0; right: 0; top: 62px;
    display: flex;
    flex-direction: column;
    align-items: center;
    color: var(--brand-blue);
    font-family: "Catamaran", sans-serif;
    font-weight: 800;
  }
  .brand-row { display: flex; align-items: center; gap: 34px; }
  .brand-dot {
    width: 196px; height: 196px; border-radius: 50%;
    background: var(--brand-orange);
    flex: none;
  }
  .brand-name {
    display: flex;
    flex-direction: column;
    font-size: 108px;
    line-height: 0.9;
    letter-spacing: -1px;
  }
  .brand-services {
    font-size: 29px;
    line-height: 1;
    margin-top: 18px;
    letter-spacing: 1.5px;
  }

  .person {
    position: absolute;
    left: 318px; width: 564px; top: 346px;
    text-align: center;
    color: var(--paper);
  }
  .person-name { font-weight: 700; font-size: 44px; line-height: 1; }
  .person-role { font-weight: 300; font-size: 27px; line-height: 1; margin-top: 4px; letter-spacing: 0.5px; }

  .contact {
    position: absolute;
    top: 491px;
    list-style: none;
    color: var(--paper);
    font-family: "Questrial", sans-serif;
    font-size: 29px;
    text-transform: uppercase;
    letter-spacing: 0.5px;
  }
  .contact li { display: flex; align-items: center; height: 46px; }
  .contact-left { left: 42px; }
  .contact-right { left: 624px; }
  .contact-icon { width: 32px; height: 32px; margin-right: 28px; flex: none; }
  .contact .address { align-items: flex-start; height: auto; }
  .address .contact-icon { margin-top: 7px; }
  .address-lines { font-style: normal; line-height: 46px; }

  .license {
    position: absolute;
    left: 0; right: 0; top: 614px;
    text-align: center;
    color: var(--paper);
    font-size: 25px;
    font-weight: 400;
  }
</style>
</head>
<body>
<main class="card">
  <svg class="card-shapes" width="1200" height="686" viewBox="0 0 1200 686" aria-hidden="true">
    <rect class="band-thin" x="0" y="374" width="1200" height="12" fill="var(--brand-blue)"/>
    <rect class="band-main" x="0" y="395" width="1200" height="291" fill="var(--brand-blue)"/>
    <polygon class="ribbon-outline" points="262,337 938,337 884,458 316,458" fill="var(--paper)"/>
    <polygon class="ribbon-fold" points="272,372 290,337 300,372" fill="var(--orange-fold)"/>
    <polygon class="ribbon-fold" points="928,372 910,337 900,372" fill="var(--orange-fold)"/>
    <polygon class="ribbon" points="290,337 910,337 872,448 328,448" fill="var(--brand-orange)"/>
  </svg>

  <header class="brand">
    <div class="brand-row">
      <span class="brand-dot"></span>
      <span class="brand-name"><span>Willow</span><span>Creek</span></span>
    </div>
    <span class="brand-services">Air Conditioning, Refrigeration, and Heating</span>
  </header>

  <section class="person">
    <h1 class="person-name">Dennis Hartwell</h1>
    <p class="person-role">OPERATOR</p>
  </section>

  <ul class="contact contact-left">
    <li>
      <svg class="contact-icon" viewBox="0 0 32 32" aria-hidden="true">
        <circle cx="16" cy="16" r="16" fill="var(--brand-orange)"/>
        <path d="M11 8.5l3 3-1.8 2.2c.9 2 2.6 3.7 4.6 4.6l2.2-1.8 3 3-1.8 2.5c-5.5-.4-11-5.9-11.4-11.4z" fill="var(--paper)"/>
      </svg>
      <span>516.738.2945</span>
    </li>
    <li>
      <svg class="contact-icon" viewBox="0 0 32 32" aria-hidden="true">
        <circle cx="16" cy="16" r="16" fill="var(--brand-orange)"/>
        <rect x="9" y="11" width="14" height="11" rx="1" fill="var(--paper)"/>
        <path d="M9.5 11.5l6.5 5 6.5-5" fill="none" stroke="var(--brand-orange)" stroke-width="1.6"/>
      </svg>
      <span>dennis@pinefieldhvac.example</span>
    </li>
  </ul>

  <ul class="contact contact-right">
    <li class="address">
      <svg class="contact-icon" viewBox="0 0 32 32" aria-hidden="true">
        <circle cx="16" cy="16" r="16" fill="var(--brand-orange)"/>
        <path d="M16 7a6 6 0 0 0-6 6c0 4.5 6 12 6 12s6-7.5 6-12a6 6 0 0 0-6-6z" fill="var(--paper)"/>
        <circle cx="16" cy="13" r="2.3" fill="var(--brand-orange)"/>
      </svg>
      <address class="address-lines">
        PO Box 782, 527 Tamsworth<br>Rd, Fernbrook, NY 11802
      </address>
    </li>
  </ul>

  <p class="license">H8179524000 Insured</p>
</main>
</body>
</html>
```